Lantern Method of Ascent Programme Graphic

Please refer to attached graphic.
I wish to redesign this graphic to represent a programme of work that we (Vendro) deliver to our customers.
The design represents 9 steps ( 3 steps at each of 3 levels) and is all about implementing the 'Lantern Method of Ascent'

I like the fact that the increasing business growth is evident when you are progressing through the stages, but the current graphic looks dated and the colours are not working.
I would also like to incorporate the LMA logo we have created.

Target Market(s)

IT Sector - businesses looking to grow

Industry/Entity Type

We are a digital marketing company

Requirements
Must have
• Clear, concise design
Should not have
• Design must not be complicated

```html
<!DOCTYPE html>
<html lang="en">
<head>
<meta charset="utf-8">
<title>Business Value – Lantern Method of Ascent</title>
<link rel="stylesheet" href="https://fonts.googleapis.com/css2?family=Lato:wght@700;900&display=swap">
<style>
  :root {
    --bg: #cfdbe6;
    --blue: #1b8fd2;
    --green: #7ab317;
    --orange: #f07a1a;
    --ink: #444b54;
    --paper: #ffffff;
    --deco: #9cc4e0;
  }
  html, body {
    margin: 0;
    padding: 0;
    overflow: hidden;
    background: var(--bg);
  }
  .canvas {
    width: 1200px;
    height: 1200px;
    position: relative;
    background: var(--bg);
    overflow: hidden;
  }
  .canvas svg { display: block; }
  .brand, .title { font-family: "Lato", sans-serif; font-weight: 900; fill: var(--blue); }
  .step-label { font-family: "Lato", sans-serif; font-weight: 900; fill: var(--ink); font-size: 25px; }
  .step-num { font-family: "Lato", sans-serif; font-weight: 900; font-size: 60px; }
  .step-name { font-family: "Lato", sans-serif; font-weight: 900; font-size: 22px; }
  .item { font-family: "Lato", sans-serif; font-weight: 900; font-size: 22px; }
  .is-green { fill: var(--green); }
  .is-orange { fill: var(--orange); }
  .is-ink { fill: var(--ink); }
  .paper { fill: var(--paper); }
  .deco { fill: var(--deco); }
</style>
</head>
<body>
<div class="canvas">
<svg width="1200" height="1200" viewBox="0 0 1000 1000" xmlns="http://www.w3.org/2000/svg">
  <defs>
    <linearGradient id="band-right" gradientUnits="userSpaceOnUse" x1="290" y1="0" x2="660" y2="0">
      <stop offset="0" stop-color="#a3a3a3"/>
      <stop offset="0.5" stop-color="#c4c4c4"/>
      <stop offset="0.85" stop-color="#eeeeee"/>
      <stop offset="1" stop-color="#ffffff"/>
    </linearGradient>
    <linearGradient id="band-left" gradientUnits="userSpaceOnUse" x1="710" y1="0" x2="340" y2="0">
      <stop offset="0" stop-color="#a3a3a3"/>
      <stop offset="0.5" stop-color="#c4c4c4"/>
      <stop offset="0.85" stop-color="#eeeeee"/>
      <stop offset="1" stop-color="#ffffff"/>
    </linearGradient>
    <linearGradient id="curl-shade" x1="0" y1="0" x2="0" y2="1">
      <stop offset="0" stop-color="#000" stop-opacity="0"/>
      <stop offset="0.55" stop-color="#000" stop-opacity="0"/>
      <stop offset="1" stop-color="#000" stop-opacity="0.12"/>
    </linearGradient>
    <filter id="soft" x="-10%" y="-10%" width="120%" height="130%">
      <feDropShadow dx="0" dy="3" stdDeviation="3" flood-color="#000" flood-opacity="0.18"/>
    </filter>
  </defs>

  <!-- brand -->
  <text class="brand" x="160" y="145" font-size="64">LMA</text>
  <text class="title" x="355" y="145" font-size="66" letter-spacing="-0.5">BUSINESS VALUE</text>

  <!-- growth chart decoration -->
  <g class="growth-chart">
    <rect class="deco" x="0" y="960" width="28" height="40"/>
    <rect class="deco" x="45" y="915" width="28" height="85"/>
    <rect class="deco" x="90" y="935" width="28" height="65"/>
    <rect class="deco" x="135" y="895" width="28" height="105"/>
    <rect class="deco" x="180" y="870" width="28" height="130"/>
    <polyline points="0,930 90,870 150,910 245,840" fill="none" stroke="var(--deco)" stroke-width="10" stroke-linejoin="round"/>
    <polygon class="deco" points="225,822 268,825 255,865"/>
  </g>

  <!-- tier 3 : ribbon back + curl, then front face -->
  <g class="tier tier-3">
    <g filter="url(#soft)">
      <path d="M1000,372 H335 A45,71.5 0 0 0 335,515 H1000 Z" fill="url(#band-right)"/>
      <path d="M1000,372 H335 A45,71.5 0 0 0 335,515 H1000 Z" fill="url(#curl-shade)"/>
    </g>
    <path filter="url(#soft)" class="paper" d="M335,305 H540 L510,262 L645,375 L510,490 L540,445 H335 A45,70 0 0 1 290,375 A45,70 0 0 1 335,305 Z"/>
  </g>

  <!-- tier 2 -->
  <g class="tier tier-2">
    <g filter="url(#soft)">
      <path d="M0,558 H665 A45,71 0 0 1 665,700 H0 Z" fill="url(#band-left)"/>
      <path d="M0,558 H665 A45,71 0 0 1 665,700 H0 Z" fill="url(#curl-shade)"/>
    </g>
    <path filter="url(#soft)" class="paper" d="M665,490 H460 L495,445 L355,560 L495,675 L460,630 H665 A45,70 0 0 0 710,560 A45,70 0 0 0 665,490 Z"/>
  </g>

  <!-- tier 1 -->
  <g class="tier tier-1">
    <g filter="url(#soft)">
      <path d="M1000,745 H335 A45,71.5 0 0 0 335,888 H1000 Z" fill="url(#band-right)"/>
      <path d="M1000,745 H335 A45,71.5 0 0 0 335,888 H1000 Z" fill="url(#curl-shade)"/>
    </g>
    <path filter="url(#soft)" class="paper" d="M335,675 H540 L505,632 L645,745 L505,860 L540,815 H335 A45,70 0 0 1 290,745 A45,70 0 0 1 335,675 Z"/>
  </g>

  <!-- tier 3 content -->
  <text class="step-label" x="420" y="368" text-anchor="middle">MONTHLY</text>
  <text class="step-label" x="420" y="400" text-anchor="middle">SCORECARD</text>
  <g class="icon-documents">
    <rect x="540" y="332" width="40" height="52" fill="#fff" stroke="#9aa" stroke-width="1.5"/>
    <rect x="545" y="337" width="30" height="4" fill="#4a5563"/>
    <rect x="545" y="346" width="22" height="3" fill="#3aaee0"/>
    <rect x="545" y="353" width="30" height="2" fill="#bbb"/>
    <rect x="545" y="359" width="30" height="2" fill="#bbb"/>
    <rect x="528" y="344" width="40" height="50" fill="#fff" stroke="#9aa" stroke-width="1.5"/>
    <rect x="533" y="350" width="12" height="4" fill="#3aaee0"/>
    <rect x="533" y="358" width="30" height="2" fill="#bbb"/>
    <rect x="533" y="364" width="30" height="2" fill="#bbb"/>
    <rect x="535" y="360" width="40" height="62" fill="#fff" stroke="#9aa" stroke-width="1.5"/>
    <rect x="555" y="372" width="16" height="8" fill="#f39221"/>
    <rect x="540" y="385" width="30" height="2" fill="#bbb"/>
    <rect x="540" y="391" width="30" height="2" fill="#bbb"/>
    <rect x="540" y="397" width="30" height="2" fill="#bbb"/>
    <rect x="513" y="363" width="42" height="56" fill="#fff" stroke="#9aa" stroke-width="1.5"/>
    <rect x="518" y="369" width="32" height="5" fill="#e84c3d"/>
    <rect x="518" y="380" width="32" height="2" fill="#bbb"/>
    <rect x="518" y="386" width="32" height="2" fill="#bbb"/>
    <rect x="518" y="393" width="18" height="6" fill="#e84c3d"/>
    <rect x="518" y="404" width="32" height="2" fill="#bbb"/>
    <rect x="518" y="410" width="32" height="2" fill="#bbb"/>
  </g>
  <text class="step-num is-green" x="700" y="444" text-anchor="middle">03</text>
  <text class="step-name is-green" x="701" y="474" text-anchor="middle">ASCENT</text>
  <g class="items">
    <rect class="is-green" x="802" y="395" width="8" height="8"/>
    <text class="item is-green" x="825" y="408">SALES</text>
    <rect class="is-green" x="802" y="429" width="8" height="8"/>
    <text class="item is-green" x="825" y="442">NURTURE</text>
    <rect class="is-green" x="802" y="468" width="8" height="8"/>
    <text class="item is-green" x="825" y="481">REFERENCE</text>
  </g>

  <!-- tier 2 content -->
  <g class="icon-briefcase">
    <path d="M452,528 V520 A6,6 0 0 1 458,514 H478 A6,6 0 0 1 484,520 V528" fill="none" stroke="#3e444c" stroke-width="5"/>
    <rect x="424" y="528" width="88" height="58" rx="6" fill="#3e444c"/>
    <rect x="424" y="528" width="88" height="26" rx="6" fill="#2f343a"/>
    <rect x="463" y="550" width="10" height="10" rx="1.5" fill="#c9ced3"/>
  </g>
  <text class="step-label" x="612" y="552" text-anchor="middle">WEEKLY</text>
  <text class="step-label" x="612" y="584" text-anchor="middle">SCORECARD</text>
  <text class="step-num is-ink" x="310" y="634" text-anchor="middle">02</text>
  <text class="step-name is-ink" x="310" y="660" text-anchor="middle">METHOD</text>
  <g class="items">
    <text class="item is-ink" x="186" y="598" text-anchor="end">MESSAGING</text>
    <rect class="is-ink" x="196" y="586" width="7" height="7"/>
    <text class="item is-ink" x="186" y="634" text-anchor="end">LEADS</text>
    <rect class="is-ink" x="196" y="622" width="7" height="7"/>
    <text class="item is-ink" x="186" y="671" text-anchor="end">PIPELINE</text>
    <rect class="is-ink" x="196" y="659" width="7" height="7"/>
  </g>

  <!-- tier 1 content -->
  <text class="step-label" x="414" y="741" text-anchor="middle">FOUNDATION</text>
  <text class="step-label" x="414" y="773" text-anchor="middle">METRIC</text>
  <g class="icon-bar-chart">
    <path d="M526,705 V778 H610" fill="none" stroke="#666" stroke-width="2"/>
    <rect x="535" y="745" width="8" height="30" fill="#e84c3d"/>
    <rect x="549" y="721" width="8" height="54" fill="#8cc63f"/>
    <rect x="563" y="735" width="8" height="40" fill="#4a5563"/>
    <rect x="577" y="716" width="8" height="59" fill="#3aaee0"/>
    <rect x="591" y="728" width="8" height="47" fill="#f39221"/>
  </g>
  <text class="step-num is-orange" x="697" y="825" text-anchor="middle">01</text>
  <text class="step-name is-orange" x="701" y="852" text-anchor="middle">LANTERN</text>
  <g class="items">
    <rect class="is-orange" x="802" y="771" width="8" height="8"/>
    <text class="item is-orange" x="825" y="784">PERSONAS</text>
    <rect class="is-orange" x="802" y="807" width="8" height="8"/>
    <text class="item is-orange" x="825" y="820">DATABASE</text>
    <rect class="is-orange" x="802" y="844" width="8" height="8"/>
    <text class="item is-orange" x="825" y="857">SYSTEM</text>
  </g>
</svg>
</div>
</body>
</html>
```